Graphic Design for Free Community Event

We need a graphic created for a community event that is aimed at families with younger children called Totz Jam. This is a free event and has a fair/carnival feel to it with rides, games, and food. I need the graphic to be flexible enough to be able to be modified and used in a variety of ways on different print and digital marketing materials. I also need the centerpiece of the design to be an event logo that can be used as a standalone element.

The overall feel needs to be fun and friendly with a slightly modern edge to it. Attached are some images used in past events. These are for reference only and do not need to be simulated or used in the final product.

Target Market(s)

Families with children

Industry/Entity Type

Church

Font styles to use
Sans Serif

Requirements
Must have
• - Logo that incorporates the event name- Event Date: August 20 - Event Time: 10am - 2pm - Church name and logo incorporated: Bright Harbor Community Church (see attached logo files)
Nice to have
• - Bright colors- Flexible design elements that are interchangeable and scalable for use of the design in different layouts across different mediums and materials.
Should not have
• - Any references or images related to drugs, alcohol, tobacco, or other subjects that would be inappropriate for children.

```html
<!DOCTYPE html>
<html lang="en">
<head>
<meta charset="utf-8">
<title>Totz Jam Flyer</title>
<link rel="stylesheet" href="https://fonts.googleapis.com/css2?family=Alfa+Slab+One&family=Montserrat:wght@500&family=Oswald:wght@700&family=Rubik+Dirt&display=swap">
<style>
  :root {
    --stage: #ffffff;
    --paper: #ffffff;
    --navy: #2e3677;
    --navy-deep: #222a63;
    --orange: #ee7a10;
    --brown: #6e3412;
    --blue-light: #3fa5d9;
    --blue-deep: #173c87;
    --shadow-blue: #0f2357;
    --gold: #ffd21a;
    --amber: #f29a0c;
    --tick: #f6b90f;
    --ink: #111111;
    --red: #b5150f;
    --white: #ffffff;
  }
  html, body {
    margin: 0;
    width: 1200px;
    height: 1000px;
    overflow: hidden;
    background: var(--stage);
  }
  .flyer {
    position: absolute;
    left: 279px;
    top: 38px;
    width: 642px;
    height: 912px;
    background: var(--paper);
  }
  .flyer svg { display: block; }
  .title { font-family: "Rubik Dirt", "Impact", sans-serif; }
  .event-date, .web-address { font-family: "Alfa Slab One", "Georgia", serif; }
  .activity, .free-tag { font-family: "Oswald", "Arial Narrow", sans-serif; font-weight: 700; }
  .church-name { font-family: "Montserrat", "Helvetica", sans-serif; font-weight: 500; fill: var(--ink); }
  .event-date { fill: var(--white); stroke: var(--brown); stroke-width: 8; paint-order: stroke; stroke-linejoin: round; }
  .activity { fill: var(--white); font-size: 40px; }
  .tick-ring { fill: none; stroke: var(--tick); stroke-width: 2.5; }
  .tick-mark { fill: none; stroke: var(--tick); stroke-width: 3.5; stroke-linecap: round; stroke-linejoin: round; }
  .polaroid-frame { fill: var(--white); }
  .free-tag { stroke: var(--brown); stroke-width: 7; paint-order: stroke; stroke-linejoin: round; }
</style>
</head>
<body>
<div class="flyer">
  <svg width="642" height="912" viewBox="0 0 642 912" xmlns="http://www.w3.org/2000/svg">
    <defs>
      <linearGradient id="titleFill" x1="0" y1="0" x2="0" y2="1">
        <stop offset="0" stop-color="var(--blue-light)"/>
        <stop offset="1" stop-color="var(--blue-deep)"/>
      </linearGradient>
      <linearGradient id="freeFill" x1="0" y1="0" x2="0" y2="1">
        <stop offset="0" stop-color="var(--gold)"/>
        <stop offset="1" stop-color="var(--amber)"/>
      </linearGradient>
      <linearGradient id="crowdFade" x1="0" y1="0" x2="1" y2="0">
        <stop offset="0" stop-color="#5a5f8e"/>
        <stop offset="0.55" stop-color="var(--navy)"/>
        <stop offset="1" stop-color="var(--navy-deep)"/>
      </linearGradient>
    </defs>

    <!-- navy backdrop band -->
    <path class="backdrop-band" role="img" aria-label="Faded photo of a crowd at an outdoor fair"
      fill="url(#crowdFade)"
      d="M540 0 H642 V688 L620 694 L600 684 L560 692 L500 686 L420 694 L340 686 L260 692 L180 684 L100 694 L40 686 L0 690 V300 L200 280 L540 240 Z"/>

    <!-- orange brush band -->
    <path class="headline-band" fill="var(--orange)"
      d="M0 55 L30 50 L120 44 L118 40 L260 30 L400 18 L520 8 L560 2 L600 6 L596 14 L612 40 L606 120 L612 200 L606 260 L612 285 L540 290 L420 300 L300 312 L180 326 L60 342 L0 350 Z"/>

    <!-- title -->
    <g transform="rotate(-3 311 150)">
      <text class="title" x="317" y="253" text-anchor="middle" font-size="230" textLength="545" lengthAdjust="spacingAndGlyphs" fill="var(--shadow-blue)">TOTZ JAM</text>
      <text class="title" x="311" y="247" text-anchor="middle" font-size="230" textLength="545" lengthAdjust="spacingAndGlyphs" fill="url(#titleFill)">TOTZ JAM</text>
    </g>

    <!-- date and time -->
    <text class="event-date" x="325" y="300" text-anchor="middle" font-size="58" textLength="560" lengthAdjust="spacingAndGlyphs" transform="rotate(-6.5 325 300)">August 20 - 10am - 2pm</text>

    <!-- activity checklist -->
    <g class="checklist">
      <g transform="translate(57 410)"><circle class="tick-ring" r="12"/><path class="tick-mark" d="M-6 0 L-1 5 L12 -10"/></g>
      <text class="activity" x="78" y="425">BUNGEE JUMP</text>
      <g transform="translate(57 456)"><circle class="tick-ring" r="12"/><path class="tick-mark" d="M-6 0 L-1 5 L12 -10"/></g>
      <text class="activity" x="80" y="471">FOOD</text>
      <g transform="translate(60 502)"><circle class="tick-ring" r="12"/><path class="tick-mark" d="M-6 0 L-1 5 L12 -10"/></g>
      <text class="activity" x="84" y="517">ROCKWALL</text>
      <g transform="translate(62 548)"><circle class="tick-ring" r="12"/><path class="tick-mark" d="M-6 0 L-1 5 L12 -10"/></g>
      <text class="activity" x="88" y="563">RIDES</text>
      <g transform="translate(64 594)"><circle class="tick-ring" r="12"/><path class="tick-mark" d="M-6 0 L-1 5 L12 -10"/></g>
      <text class="activity" x="92" y="609">INFLATABLES</text>
    </g>

    <!-- photo collage -->
    <g class="polaroid" transform="translate(540 390) rotate(15)">
      <rect class="polaroid-frame" x="-74" y="-66" width="148" height="132"/>
      <rect x="-64" y="-56" width="128" height="104" fill="#9fb3bf" role="img" aria-label="Child on a bungee trampoline at a fair"/>
    </g>
    <g class="polaroid" transform="translate(411 458) rotate(-10)">
      <rect class="polaroid-frame" x="-72" y="-76" width="144" height="152"/>
      <rect x="-62" y="-66" width="124" height="122" fill="#d79a5e" role="img" aria-label="Child eating a snack"/>
    </g>
    <g class="polaroid" transform="translate(544 538) rotate(15)">
      <rect class="polaroid-frame" x="-72" y="-72" width="144" height="144"/>
      <rect x="-62" y="-62" width="124" height="116" fill="#d8b43a" role="img" aria-label="Child climbing a rock wall"/>
    </g>
    <g class="polaroid" transform="translate(421 624) rotate(12)">
      <rect class="polaroid-frame" x="-72" y="-72" width="144" height="144"/>
      <rect x="-62" y="-62" width="124" height="116" fill="#7a5a3c" role="img" aria-label="Colourful carousel ride"/>
    </g>
    <g class="polaroid" transform="translate(541 702) rotate(-2)">
      <rect class="polaroid-frame" x="-66" y="-58" width="132" height="116"/>
      <rect x="-58" y="-50" width="116" height="92" fill="#ec9bb8" role="img" aria-label="Child playing on a pink inflatable"/>
    </g>

    <!-- free tag -->
    <text class="free-tag" x="176" y="712" font-size="80" textLength="160" lengthAdjust="spacingAndGlyphs" fill="url(#freeFill)">FREE</text>

    <!-- church name -->
    <g class="church">
      <circle cx="108" cy="750" r="58" fill="var(--ink)"/>
      <text class="church-name" x="188" y="752" font-size="44" textLength="262" lengthAdjust="spacingAndGlyphs">BRIGHT HARBOR</text>
      <text class="church-name" x="188" y="779" font-size="23" textLength="262" lengthAdjust="spacingAndGlyphs">COMMUNITY CHURCH</text>
    </g>

    <!-- web address banner -->
    <g transform="translate(0 8) rotate(-3 315 845)">
      <path class="web-banner" fill="var(--red)"
        d="M42 812 L120 806 L300 810 L480 804 L588 808 L592 846 L586 884 L420 880 L260 886 L100 882 L40 886 L44 850 Z"/>
      <text class="web-address" x="315" y="862" text-anchor="middle" font-size="44" textLength="520" lengthAdjust="spacingAndGlyphs"><tspan fill="var(--white)">www.</tspan><tspan fill="var(--gold)">brightharborchurch</tspan><tspan fill="var(--white)">.com</tspan></text>
    </g>
  </svg>
</div>
</body>
</html>
```